Birchwell Entreprise Campus Media Package

We are looking for a designer to unify our company's image throughout its stationery and marketing deliverables. We will be focusing on:
*Business Cards (3.5 x 2)
*Letter Head (Letter Size)
*PowerPoint Presentation Template,
*One Pager Flyer (Letter Size)
*Front of Elevator's bay: 4 photos of the elevator bays (two groups of 3 elevators) to which we are looking for designs for its doors and surrounding wall (vinyl prints)
*Font's suggestions
*Official color palette.
*Outdoor Street Signage: please use the following dimensions:
Sign #1 (Richmond Side): 48(W)x72"(H) (3 sided)
Sign #2: 24"(W)x48"(H) (3 sided)
Sign #3 (Top of Hill): 30(W)x54(H) (2 sides)
*Carport Sign:
See photos attached. The white letters will be removed, and a new sign will take place. Preferably, Cut-Out fonts, but we can consider an alternative approach for cost effective solution.
Find attached the approved logos.
______________________________________
We are a real estate holding company focused on the commercial office space in the Ohio, US, market.
You can check our site at www.birchwellcampus-example.com
As inspiration guidelines, we would like to see designs that are modern, minimalistic, dynamic and energetic.
Updates
Target Market(s)
General Population, Business Owners, Non-Profit Organizations, Government
Industry/Entity Type
Real Estate - Commercial Office Space - Flex Space
Look and feel
Each slider illustrates characteristics of the customer's brand and the style your logo design should communicate.

```html
<!DOCTYPE html>
<html lang="en">
<head>
<meta charset="utf-8">
<title>Birchwell Park – Business Card</title>
<link rel="stylesheet" href="https://fonts.googleapis.com/css2?family=Montserrat:wght@600;700&display=swap">
<style>
  :root {
    --backdrop: #3c4653;
    --card-dark: #28272b;
    --card-light: #ffffff;
    --ink-light: #ffffff;
    --ink-dark: #1d1d1f;
  }
  * { margin: 0; padding: 0; box-sizing: border-box; }
  html, body { width: 1200px; height: 803px; overflow: hidden; }
  body {
    background: var(--backdrop);
    font-family: "Montserrat", Arial, sans-serif;
    position: relative;
  }
  .card {
    position: absolute;
    top: 253px;
    width: 520px;
    height: 297px;
    background: var(--card-dark);
    overflow: hidden;
    box-shadow: 0 10px 24px rgba(0,0,0,.35);
  }
  .card--front { left: 60px; }
  .card--back { left: 620px; }

  /* Front */
  .brand-name {
    position: absolute;
    left: 0; right: 0;
    top: 50%;
    transform: translateY(-50%);
    text-align: center;
    color: var(--ink-light);
    font-size: 28px;
    font-weight: 600;
    letter-spacing: 1px;
  }

  /* Back */
  .back__strip {
    position: absolute;
    left: 0; top: 0;
    width: 142px; height: 100%;
    background: var(--card-light);
  }
  .strip-name {
    position: absolute;
    left: 50%; top: 50%;
    transform: translate(-50%, -50%) rotate(-90deg);
    white-space: nowrap;
    color: var(--ink-dark);
    font-size: 22px;
    font-weight: 600;
    letter-spacing: 1px;
  }
  .contact {
    position: absolute;
    left: 176px; top: 44px;
    color: var(--ink-light);
  }
  .contact__name { font-size: 26px; font-weight: 700; letter-spacing: .5px; }
  .contact__role { font-size: 10px; font-weight: 600; letter-spacing: 1px; margin-top: 2px; }
  .contact__rule { width: 76px; height: 2px; background: var(--ink-light); margin: 6px 0 22px; }
  .contact__list { list-style: none; }
  .contact__item {
    display: flex; align-items: flex-start; gap: 12px;
    font-size: 12.5px; font-weight: 600; margin-bottom: 14px; line-height: 1.3;
  }
  .contact__icon {
    width: 20px; height: 20px; flex: none;
    border-radius: 50%; background: var(--ink-light);
    display: flex; align-items: center; justify-content: center;
  }
  .contact__icon svg { width: 11px; height: 11px; fill: var(--card-dark); }
</style>
</head>
<body>

<section class="card card--front">
  <p class="brand-name">BIRCHWELL PARK</p>
</section>

<section class="card card--back">
  <div class="back__strip">
    <p class="strip-name">BIRCHWELL PARK</p>
  </div>

  <div class="contact">
    <h1 class="contact__name">NAME SURNAME</h1>
    <p class="contact__role">DESIGNATION HERE</p>
    <div class="contact__rule"></div>
    <ul class="contact__list">
      <li class="contact__item">
        <span class="contact__icon"><svg viewBox="0 0 24 24"><path d="M6.6 10.8a15 15 0 0 0 6.6 6.6l2.2-2.2c.3-.3.7-.4 1-.2 1.1.4 2.3.6 3.6.6.6 0 1 .4 1 1V20c0 .6-.4 1-1 1A17 17 0 0 1 3 4c0-.6.4-1 1-1h3.5c.6 0 1 .4 1 1 0 1.3.2 2.5.6 3.6.1.3 0 .7-.2 1z"/></svg></span>
        555-014-0987
      </li>
      <li class="contact__item">
        <span class="contact__icon"><svg viewBox="0 0 24 24"><path d="M3 5h18v14H3zm2 2v.5l7 4.5 7-4.5V7zm0 2.9V17h14V9.9l-7 4.5z"/></svg></span>
        hello@yourcompany
      </li>
      <li class="contact__item">
        <span class="contact__icon"><svg viewBox="0 0 24 24"><path d="M12 2a7 7 0 0 0-7 7c0 5 7 13 7 13s7-8 7-13a7 7 0 0 0-7-7zm0 9.5A2.5 2.5 0 1 1 12 6.5a2.5 2.5 0 0 1 0 5z"/></svg></span>
        <span>1480 Alder Avenue,<br>Marren OH 44000</span>
      </li>
    </ul>
  </div>
</section>

</body>
</html>
```